Business Card Design Project

We need a new fresh business card for our business. There are multiple services we offer and we need a fresh corporate card that represents us better. We start from cleaning carpet and tiles, to upholstery and curtains, to completely clean all contents and building materials after a fire, or completely dry out a home or business after a major or minor flood event. We are open to all concepts as we want to create a new look, maybe even logo, signage, vehicle signage, uniforms.
We are open to new colours etc.

Go to www.brightmoorcare.com.au for current logo and all other past ideas

Target Market(s)

Everyone is our possible client but we are targeting more coorporate

Industry/Entity Type

Building

```html
<!DOCTYPE html>
<html lang="en">
<head>
<meta charset="utf-8">
<title>Brightmoor Care – Business Card</title>
<link href="https://fonts.googleapis.com/css2?family=Michroma&family=Open+Sans:wght@400;600&display=swap" rel="stylesheet">
<style>
  :root {
    --brand-blue: #1a5ea3;
    --brand-pink: #e0207a;
    --card-white: #ffffff;
    --ink-dark: #2b2b2b;
    --backdrop: #e9eaec;
  }
  * { box-sizing: border-box; margin: 0; padding: 0; }
  html, body { width: 1200px; height: 900px; overflow: hidden; }
  body {
    background: var(--backdrop);
    display: flex; align-items: center; justify-content: center;
  }
  .business-card {
    position: relative;
    width: 900px; height: 520px;
    background: var(--card-white);
    border-radius: 46px;
    overflow: hidden;
    box-shadow: 0 10px 30px rgba(0,0,0,.15);
  }
  .card-waves { position: absolute; inset: 0; }
  .brand-lockup {
    position: absolute; top: 48px; right: 70px;
    display: flex; align-items: center; gap: 14px;
  }
  .brand-lockup__dot {
    width: 56px; height: 56px; border-radius: 50%;
    background: var(--brand-blue);
  }
  .brand-lockup__name {
    font-family: "Michroma", sans-serif;
    font-size: 28px; color: var(--brand-blue);
  }
  .holder {
    position: absolute; left: 70px; top: 236px;
  }
  .holder__name {
    font-family: "Michroma", sans-serif;
    font-size: 25px; color: var(--brand-blue); letter-spacing: 1px;
  }
  .holder__title {
    font-family: "Open Sans", sans-serif; font-weight: 600;
    font-size: 19px; color: var(--ink-dark); margin-top: 2px;
  }
  .contact-list {
    position: absolute; left: 70px; bottom: 34px;
    list-style: none;
    font-family: "Michroma", sans-serif; font-size: 14px;
    color: var(--card-white);
  }
  .contact-list li {
    display: flex; align-items: center; gap: 14px; height: 27px;
  }
  .contact-list svg { width: 16px; height: 16px; fill: var(--card-white); flex: none; }
  .office-address {
    position: absolute; right: 70px; top: 236px;
    font-family: "Michroma", sans-serif; font-size: 17px; line-height: 1.55;
    color: var(--card-white); text-align: right;
  }
</style>
</head>
<body>
  <div class="business-card">
    <svg class="card-waves" viewBox="0 0 900 520" preserveAspectRatio="none" aria-hidden="true">
      <path d="M0,345 C260,330 560,270 900,140 L900,520 L0,520 Z" fill="var(--brand-blue)"/>
      <path d="M430,318 C640,275 790,205 900,110 L900,132 C790,222 640,290 430,318 Z" fill="var(--brand-pink)"/>
      <path d="M40,340 C240,300 480,285 720,205 C500,270 260,305 40,340 Z" fill="var(--brand-blue)"/>
    </svg>

    <div class="brand-lockup">
      <span class="brand-lockup__name">Brightmoor Care</span>
      <span class="brand-lockup__dot"></span>
    </div>

    <div class="holder">
      <div class="holder__name">DANIEL MERCER</div>
      <div class="holder__title">Managing Director</div>
    </div>

    <ul class="contact-list">
      <li><svg viewBox="0 0 24 24"><path d="M6.6 10.8a15 15 0 0 0 6.6 6.6l2.2-2.2a1 1 0 0 1 1-.25 11 11 0 0 0 3.6.6 1 1 0 0 1 1 1V20a1 1 0 0 1-1 1A17 17 0 0 1 3 4a1 1 0 0 1 1-1h3.5a1 1 0 0 1 1 1 11 11 0 0 0 .6 3.6 1 1 0 0 1-.25 1z"/></svg>021 555 0148</li>
      <li><svg viewBox="0 0 24 24"><path d="M7 1h10a2 2 0 0 1 2 2v18a2 2 0 0 1-2 2H7a2 2 0 0 1-2-2V3a2 2 0 0 1 2-2zm0 3v14h10V4zm5 15.5a1.2 1.2 0 1 0 0 2.4 1.2 1.2 0 0 0 0-2.4z"/></svg>021 555 0149</li>
      <li><svg viewBox="0 0 24 24"><path d="M6 2h9l3 3v4h2a2 2 0 0 1 2 2v9H2v-9a2 2 0 0 1 2-2h2zm2 2v5h8V6h-2V4zm-2 9v2h12v-2z"/></svg>021 555 0150</li>
      <li><svg viewBox="0 0 24 24"><path d="M2 5h20v14H2zm2 2v.5l8 5 8-5V7zm0 3v7h16v-7l-8 5z"/></svg>info@brightmoorcare.com.au</li>
      <li><svg viewBox="0 0 24 24"><path d="M12 2a10 10 0 1 0 0 20 10 10 0 0 0 0-20zm6.9 9h-3a15 15 0 0 0-1.3-5.6A8 8 0 0 1 18.9 11zM12 4c.9 1.2 1.8 3.8 1.9 7h-3.8C10.2 7.8 11.1 5.2 12 4zM9.4 5.4A15 15 0 0 0 8.1 11h-3a8 8 0 0 1 4.3-5.6zM5.1 13h3a15 15 0 0 0 1.3 5.6A8 8 0 0 1 5.1 13zM12 20c-.9-1.2-1.8-3.8-1.9-7h3.8c-.1 3.2-1 5.8-1.9 7zm2.6-1.4a15 15 0 0 0 1.3-5.6h3a8 8 0 0 1-4.3 5.6z"/></svg>www.brightmoorcare.com.au</li>
    </ul>

    <address class="office-address" style="font-style:normal">12 Harbour St, Level 4<br>Northgate NSW</address>
  </div>
</body>
</html>
```